Marquise Velvet Stable Goods - Elite line of horse care grooming products

I wanted to have a label design for my equestrian products that made the people who use them on their horses feel like a princess. I use all natural ingredients, they smell wonderful and work! I think my current design could be more amazing.... I have a total of 6 products. The final design should communicate that you are using the finest and highest quality ingredients on your best friend. please see my website (www.MarquiseStable.example) for the design aesthetic I'm going for. Design Guide:
The design should communicate that you are using the finest and highest quality ingredients on your best friend.
Create a bold, unique, visually-appealing design
Make buyer feel like a princess
Impart that you are taking care of your horse because you’re buying the best
Stand out from most other products currently on the market that look boring/outdated, bland
Avoid any design or visual images that impart chemical, industrial or commercial connotations
Key Terms: Elite, Bold, Serious, Baroque elegance, Feminine, Elegance, Wow, Fairytale, Fantasy, Elegance,

Please create: Design separate front and back BOPP labels for 32oz. spray bottle, 3.5x5” Rosemary, Lavender & Mint Insect Repellent

Design should convey a sense of wealth and prestige
Elegance & sophistication
Professional quality

Design Guide:

Key Attributes of Product:
Expensive product
Therapeutic-grade essential oils
All-natural ingredients
No poisons or pesticides
Smell wonderful
They work

Please use royal purple and gold

Target Market(s)

High end female horse owners..12-65yo female horse owners who want to and can afford to buy premium products for horse grooming.

Font styles to use
Sans Serif
Decorative
Script

Colors
876aae

Requirements
Must have
• Elegance, wow, pick me. Mandatory Graphics:
• Marquise Velvet Stable Goods logo with gold doily (no gradient on gold)
Nice to have
• Fairytale, fantasy, quality, elite, smells good,
Should not have
• I do not want my bottles to look like pesticides or poison.

```html
<!DOCTYPE html>
<html lang="en">
<head>
<meta charset="utf-8">
<title>Marquise Velvet Stable Goods – Natural Insect Repellent Label</title>
<link href="https://fonts.googleapis.com/css2?family=Montserrat:wght@500;600;700&family=Open+Sans:wght@400&family=Pinyon+Script&display=swap" rel="stylesheet">
<style>
  :root {
    --backdrop: #5e217a;
    --royal-purple: #4a1470;
    --royal-purple-deep: #3a0d5a;
    --brand-purple: #6a2f9a;
    --gold: #c9a06a;
    --gold-dark: #a87c48;
    --label-white: #ffffff;
    --pattern-light: #f1eef3;
    --pattern-mid: #e4dde8;
    --text-light: #f3eef8;
  }
  * { box-sizing: border-box; margin: 0; padding: 0; }
  html, body {
    width: 1200px;
    height: 1099px;
    overflow: hidden;
    background: var(--backdrop);
  }
  .canvas {
    position: relative;
    width: 1200px;
    height: 1099px;
  }
  .label {
    position: absolute;
    left: 280px;
    top: 90px;
    width: 640px;
    height: 920px;
    background: var(--label-white);
    box-shadow: 0 10px 30px rgba(0,0,0,0.25);
  }
  .label__pattern {
    position: absolute;
    left: 0; top: 0;
    width: 640px;
    height: 655px;
    background: linear-gradient(160deg, var(--pattern-light) 0%, var(--label-white) 45%, var(--pattern-mid) 100%);
  }
  .label__panel {
    position: absolute;
    left: 148px;
    top: 27px;
    width: 352px;
    height: 451px;
    background: var(--label-white);
    border: 4px solid var(--gold);
    display: flex;
    flex-direction: column;
    align-items: center;
  }
  .brand {
    margin-top: 150px;
    display: flex;
    flex-direction: column;
    align-items: center;
    font-family: "Montserrat", sans-serif;
    font-weight: 600;
    color: var(--brand-purple);
    text-align: center;
    font-size: 22px;
    line-height: 1.25;
    letter-spacing: 0.5px;
  }
  .product-title {
    margin-top: auto;
    margin-bottom: 14px;
    text-align: center;
  }
  .product-title__script {
    font-family: "Pinyon Script", cursive;
    font-size: 78px;
    line-height: 0.9;
    color: var(--gold-dark);
  }
  .product-title__name {
    font-family: "Montserrat", sans-serif;
    font-weight: 700;
    font-size: 23px;
    letter-spacing: 3.5px;
    color: var(--brand-purple);
  }
  .blend-band {
    position: absolute;
    left: 96px;
    top: 561px;
    width: 467px;
    height: 48px;
    background: var(--gold);
    display: flex;
    align-items: center;
    justify-content: center;
    font-family: "Montserrat", sans-serif;
    font-weight: 700;
    font-size: 19px;
    color: var(--royal-purple);
    letter-spacing: 0.3px;
  }
  .label__info {
    position: absolute;
    left: 0;
    top: 655px;
    width: 640px;
    height: 265px;
    background: linear-gradient(90deg, var(--royal-purple-deep), var(--royal-purple) 50%, var(--royal-purple-deep));
    border-top: 3px solid var(--gold);
    color: var(--text-light);
    text-align: center;
  }
  .benefits {
    list-style: none;
    padding-top: 18px;
    font-family: "Open Sans", sans-serif;
    font-size: 17px;
    line-height: 25px;
  }
  .tagline {
    margin-top: 18px;
    font-family: "Pinyon Script", cursive;
    font-size: 40px;
    line-height: 1;
  }
  .volume {
    position: absolute;
    right: 16px;
    bottom: 28px;
    font-family: "Open Sans", sans-serif;
    font-size: 17px;
  }
  .label__info-rule {
    position: absolute;
    left: 0;
    bottom: 14px;
    width: 640px;
    height: 3px;
    background: var(--gold);
  }
</style>
</head>
<body>
  <main class="canvas">
    <section class="label" aria-label="Front label, Natural Insect Repellent">
      <div class="label__pattern" role="img" aria-label="Geometric line pattern in purple and gold on white"></div>

      <div class="label__panel">
        <div class="brand">
          <span>Marquise Velvet</span>
          <span>Stable Goods</span>
        </div>
        <h1 class="product-title">
          <span class="product-title__script">Natural</span><br>
          <span class="product-title__name">INSECT REPELLENT</span>
        </h1>
      </div>

      <div class="blend-band">LAVENDER, MINT &amp; ROSEMARY BLEND</div>

      <div class="label__info">
        <ul class="benefits">
          <li>Quality ingredients made with therapeutic grade essential oils..</li>
          <li>and it works!</li>
          <li>Free of harsh chemicals, lovely smell.</li>
          <li>Provides a protective barrier from insect bites to prevent itching.</li>
          <li>Promotes healthy hair growth and soft skin.</li>
        </ul>
        <p class="tagline">Love your horse!</p>
        <span class="volume">8.oz</span>
        <div class="label__info-rule"></div>
      </div>
    </section>
  </main>
</body>
</html>
```